Business Card Design

We need a business card for a well established Semi Trailer Hire company. I am looking for a new start as we are moving so would like to update our Business Cards and Letter heads.
We hire Semi Trailers to Transport companies.
The colour of our Trailers are Cherry Red so this must be the prominent colour.
I do not want any pictures of trailers on the design.
I do not want the design to be flowery in anyway as we are in the transport industry.
Simple yet effective

Trovan Hire Pty Ltd
Ros Dunmore
Director
Ph: 03 9412 5083
Mobile: 0421 736 209
ros.dunmore@trovanhire.com.au
www.trovanhire.com.au
214-220 Pellow Road, Yarraville

```html
<!DOCTYPE html>
<html lang="en">
<head>
<meta charset="utf-8">
<title>Trovan Hire Pty Ltd – Business Card</title>
<link rel="stylesheet" href="https://fonts.googleapis.com/css2?family=Fira+Sans+Extra+Condensed:wght@600&family=Source+Sans+3:ital,wght@0,400;1,400&display=swap">
<style>
  :root {
    --cherry: #c4162c;
    --cherry-light: #e27a88;
    --ink: #000000;
    --paper: #ffffff;
    --guide: #29abe2;
    --flag-navy: #25306b;
  }
  html, body {
    margin: 0;
    padding: 0;
    width: 1200px;
    height: 733px;
    overflow: hidden;
    background: var(--paper);
  }
  .card {
    position: relative;
    width: 1200px;
    height: 733px;
    background: var(--cherry);
    overflow: hidden;
    color: var(--paper);
    font-family: "Source Sans 3", sans-serif;
  }
  .card > * { position: absolute; margin: 0; }

  .ornament-area {
    left: 795px; top: 275px;
    width: 405px; height: 458px;
    border-top-left-radius: 100% 100%;
    background: radial-gradient(circle at 100% 100%, var(--cherry-light) 0%, #d3475a 70%, var(--cherry) 100%);
  }

  .company {
    left: 56px; top: 46px;
    font-family: "Fira Sans Extra Condensed", sans-serif;
    font-weight: 600;
    font-size: 72px;
    line-height: 1;
  }
  .address {
    left: 56px; top: 130px;
    font-size: 40px;
    line-height: 1;
  }
  .flag {
    left: 915px; top: 53px;
    width: 227px; height: 115px;
    background: var(--flag-navy);
  }

  .divider {
    left: 0; top: 198px;
    width: 1200px; height: 28px;
    background: var(--ink);
  }
  .divider::after {
    content: "";
    position: absolute; left: 8px; right: 8px; top: 12px;
    border-top: 3px dashed var(--paper);
  }

  .person {
    left: 56px; top: 236px;
    font-family: "Fira Sans Extra Condensed", sans-serif;
    font-weight: 600;
    font-size: 64px;
    line-height: 1;
  }
  .contact-row { left: 56px; width: 700px; height: 70px; }
  .contact-row.phone { top: 306px; }
  .contact-row.mobile { top: 382px; }
  .contact-label {
    position: absolute; left: 0; bottom: 8px;
    font-style: italic;
    font-size: 33px;
  }
  .contact-number {
    position: absolute; left: 183px; bottom: 0;
    font-family: "Fira Sans Extra Condensed", sans-serif;
    font-weight: 600;
    font-size: 62px;
    line-height: 1;
  }

  .icon {
    top: 469px;
    width: 94px; height: 94px;
    background: var(--ink);
    border: 2px solid var(--paper);
    border-radius: 9px;
    box-sizing: border-box;
  }
  .icon svg { display: block; width: 100%; height: 100%; }
  .icon.mail { left: 59px; }
  .icon.call { left: 182px; }

  .email {
    left: 56px; top: 585px;
    font-size: 33px;
    line-height: 1;
  }

  .footer-band {
    left: 6px; right: 6px; top: 644px;
    height: 50px;
    background: var(--ink);
    display: flex;
    align-items: center;
    justify-content: center;
    font-size: 33px;
  }
  .footer-band span { margin-left: -14px; }

  .trim-guide {
    left: 28px; top: 25px;
    width: 1144px; height: 675px;
    border: 3px solid var(--guide);
    box-sizing: border-box;
  }
</style>
</head>
<body>
<main class="card">
  <div class="ornament-area" role="img" aria-label="Decorative white concentric arcs rising from the lower right corner"></div>

  <h1 class="company">Trovan Hire Pty Ltd</h1>
  <p class="address">214-220 Pellow Road, Yarraville</p>
  <div class="flag" role="img" aria-label="Australian national flag"></div>

  <div class="divider"></div>

  <h2 class="person">Ros Dunmore</h2>
  <div class="contact-row phone">
    <span class="contact-label">Director Ph:</span>
    <span class="contact-number">03 9412 5083</span>
  </div>
  <div class="contact-row mobile">
    <span class="contact-label">Mobile:</span>
    <span class="contact-number">0421 736 209</span>
  </div>

  <div class="icon mail" aria-hidden="true">
    <svg viewBox="0 0 93 93">
      <rect x="12" y="24" width="69" height="45" fill="none" stroke="#fff" stroke-width="4"/>
      <path d="M12 24 L46.5 52 L81 24 M12 69 L38 45 M81 69 L55 45" fill="none" stroke="#fff" stroke-width="4" stroke-linejoin="round"/>
    </svg>
  </div>
  <div class="icon call" aria-hidden="true">
    <svg viewBox="0 0 93 93">
      <path d="M38 14 h10 a3 3 0 0 1 3 3 v14 a3 3 0 0 1 -3 3 h-5 q-4 12 0 25 h5 a3 3 0 0 1 3 3 v14 a3 3 0 0 1 -3 3 h-10 q-16 -32 0 -65 z" fill="#fff"/>
    </svg>
  </div>

  <p class="email">ros.dunmore@trovanhire.com.au</p>

  <div class="footer-band"><span>www.trovanhire.com.au</span></div>

  <div class="trim-guide" aria-hidden="true"></div>
</main>
</body>
</html>
```